Historic Church website

We want our church website to feel warm, historic, and clean, modern, and easy to navigate. Dont use the anchor

Current website: https://www.meadowlarkfellowship.org/

Requirements
Should not have
• I would like to use the logo without the anchor

```html
<!DOCTYPE html>
<html lang="en">
<head>
<meta charset="utf-8">
<title>Meadowlark Fellowship Church</title>
<link href="https://fonts.googleapis.com/css2?family=Outfit:wght@300;400;500;600;700&display=swap" rel="stylesheet">
<style>
:root{
  --gold:#cfb53b;
  --ink:#1f1f1f;
  --black:#0a0a0a;
  --cream:#f6efe3;
  --white:#ffffff;
  --muted:#444;
  --line:#8a8a8a;
}
*{box-sizing:border-box;margin:0;padding:0}
html,body{width:1200px;height:4743px;overflow:hidden}
body{font-family:'Outfit',sans-serif;color:var(--ink);background:var(--white);position:relative}
.abs{position:absolute}
.btn{position:absolute;display:flex;align-items:center;justify-content:center;border-radius:8px;font-size:14px;font-weight:400}
.btn-gold{background:var(--gold);color:#fff}
.btn-white{background:#fff;color:var(--ink);box-shadow:0 2px 10px rgba(0,0,0,.12)}

/* hero */
.hero{left:0;top:0;width:1200px;height:605px;background:radial-gradient(ellipse at 50% 75%,#6b3a1c 0%,#3a2214 35%,#1a120c 75%,#0e0a07 100%)}
.hero-shade{left:0;top:0;width:1200px;height:605px;background:linear-gradient(rgba(0,0,0,.35),rgba(0,0,0,.1) 40%,rgba(0,0,0,.3))}
.brand{left:138px;top:30px;display:flex;align-items:center;gap:10px;color:#fff;font-size:12px;font-weight:500;letter-spacing:1.2px;line-height:15px}
.brand-dot{width:40px;height:40px;border:2px solid #fff;border-radius:50%;flex:none}
.nav{left:407px;top:43px;display:flex;gap:22px;color:#fff;font-size:14px}
.hero-title{left:0;top:212px;width:1200px;text-align:center;color:#fff;font-size:38px;font-weight:700;line-height:53px}

/* map band */
.map{left:0;top:600px;width:1200px;height:330px;background:linear-gradient(135deg,#4a3a27,#7a6447 45%,#3c2e1f)}
.map-shade{left:0;top:600px;width:1200px;height:330px;background:rgba(0,0,0,.35)}
.map-text{left:0;top:694px;width:1200px;text-align:center;color:#fff;font-size:27px;font-weight:600;line-height:35px}

/* newsletter */
.field{position:absolute;left:183px;width:372px;height:53px;background:#fff;border-radius:8px;box-shadow:0 3px 14px rgba(0,0,0,.1);padding-left:28px;display:flex;align-items:center;font-size:14px}
.news-title{left:700px;top:1065px;width:420px;text-align:center;color:#fff;font-size:40px;font-weight:600;line-height:52px}

/* about */
.about-photo{left:145px;top:1487px;width:410px;height:402px;border-radius:50%;background:radial-gradient(circle at 45% 45%,#6a4526,#2c1b10 70%)}
.about-h{left:600px;top:1468px;width:470px;font-size:28px;font-weight:600;line-height:35px}
.about-p{left:601px;width:462px;font-size:13.4px;line-height:21px;color:var(--muted)}

/* gold band */
.band-text{left:138px;top:2035px;color:#fff;font-size:27px;font-weight:600;line-height:37px}

/* visit */
.sec-title{left:0;width:1200px;text-align:center;font-size:27px;font-weight:600}
.card{position:absolute;background:#fff;border-radius:10px;box-shadow:0 4px 18px rgba(0,0,0,.12)}
.card-img{position:absolute;left:11px;top:11px;right:11px;height:195px}
.card h3{position:absolute;left:11px;font-size:18px;font-weight:600;line-height:22px}
.card .meta{position:absolute;left:11px;font-size:13px;line-height:17px}
.card .small{position:absolute;left:11px;right:11px;font-size:11.5px;line-height:12px}
.card-gold{background:var(--gold);color:#fff}

/* events */
.events{left:0;top:2685px;width:1200px;height:810px;background:var(--cream)}
.ev-img{position:absolute;left:138px;width:212px;height:150px;border-radius:4px}
.ev-date{position:absolute;left:428px;font-size:12.5px}
.ev-title{position:absolute;left:732px;font-size:18px;font-weight:600}
.ev-line{position:absolute;left:125px;width:946px;height:1px;background:var(--line)}

/* quote */
.quote{left:138px;top:3575px;width:922px;height:210px;background:#fff;box-shadow:0 4px 20px rgba(0,0,0,.1)}
.quote p{position:absolute;left:140px;top:95px;width:640px;text-align:center;font-style:italic;font-size:14px;line-height:18px}
.quote .who{position:absolute;left:0;top:170px;width:922px;text-align:center;font-size:11.5px}
.avatar{left:552px;top:3523px;width:96px;height:96px;border-radius:50%;background:radial-gradient(circle,#7a5536,#2a1a10)}

/* sermons */
.s-card h3{position:absolute;left:11px;top:220px;width:270px;font-size:18px;font-weight:600;line-height:21px}
.s-card .meta{position:absolute;left:11px;top:270px;font-size:13px}
.s-card .org{position:absolute;left:11px;top:298px;font-size:11.5px}
.s-img{position:absolute;left:12px;top:12px;right:12px;height:195px;border-radius:6px}

/* footer */
.foot-col{position:absolute;top:4415px;color:#fff}
.foot-col h4{font-size:18px;font-weight:600;margin-bottom:9px}
.foot-col li{list-style:none;font-size:13.5px;line-height:28.5px}
.foot-brand{left:138px;top:4512px;display:flex;align-items:center;gap:12px;color:#fff;font-size:18px;font-weight:500;letter-spacing:1.5px;line-height:22px}
.foot-brand .brand-dot{width:62px;height:62px}
.copy{left:138px;top:4712px;color:#fff;font-size:11.5px}
</style>
</head>
<body>

<!-- hero -->
<div class="abs hero" role="img" aria-label="Warm historic library room with leather armchairs, bookshelves and a glowing fireplace"></div>
<div class="abs hero-shade"></div>
<div class="abs brand"><span class="brand-dot"></span><span>MEADOWLARK<br>FELLOWSHIP</span></div>
<nav class="abs nav"><span>About MFC</span><span>Ministries</span><span>Bible Studies</span><span>Sermon Library</span></nav>
<div class="btn btn-gold" style="left:970px;top:35px;width:88px;height:34px;font-size:13px">Donate</div>
<h1 class="abs hero-title">ANCIENT CHURCH. ANCIENT FAITH.<br>ETERNAL TRUTH.</h1>
<div class="btn btn-gold" style="left:482px;top:333px;width:234px;height:48px">Join our Community</div>

<!-- map band -->
<div class="abs map" role="img" aria-label="Antique world map on a wooden desk"></div>
<div class="abs map-shade"></div>
<div class="abs map-text">We Have This Hope As An Anchor For The Soul<br>Firm And Secure Heb 6:19</div>
<div class="btn btn-gold" style="left:520px;top:779px;width:158px;height:48px">Join Group</div>

<!-- white wedge under map and dark curved panel -->
<svg class="abs" style="left:0;top:870px" width="1200" height="510" viewBox="0 0 1200 510">
  <path d="M0 5 L655 55 L1200 55 L1200 510 L0 510 Z" fill="#fff"/>
  <path d="M655 55 L1200 55 L1200 508 L695 508 C 610 360 590 170 655 55 Z" fill="#222"/>
</svg>
<div class="field" style="top:1010px">First Name</div>
<div class="field" style="top:1092px">Last Name</div>
<div class="field" style="top:1173px">Email</div>
<div class="btn btn-white" style="left:282px;top:1255px;width:175px;height:53px">Click To Send</div>
<div class="abs news-title">Sign Up For Our<br>Weekly Newsletter</div>
<div class="btn btn-gold" style="left:820px;top:1180px;width:175px;height:52px">Register</div>

<!-- about -->
<svg class="abs" style="left:138px;top:1482px" width="420" height="412" viewBox="0 0 420 412">
  <path d="M205 4 A 202 202 0 1 0 210 408" fill="none" stroke="#cfb53b" stroke-width="4"/>
</svg>
<div class="abs about-photo" role="img" aria-label="Dark wood library with globe, leather armchair and bookshelves"></div>
<h2 class="abs about-h">Meadowlark Fellowship Church is an independent Christian church in the Protestant tradition.</h2>
<p class="abs about-p" style="top:1577px">Its central tenets are found in its Articles of Faith and include belief in: the Deity and Lordship of Jesus Christ; the Trinity; Jesus' perfect life, atoning death on the cross, bodily resurrection, and ascension; Jesus' literal return; the inerrancy of the Bible in its original manuscripts; and our need for salvation through personal faith in Jesus Christ. In keeping with the prevailing perspective of the church during the centuries immediately following the Apostles, we teach Premillennialism.</p>
<p class="abs about-p" style="top:1752px">That is, the belief that Messiah will physically and literally return to earth at Jerusalem before the millennial age commences. At that time, he will establish a kingdom over which he will preside as King. All the promises of Israel's covenants will be literally fulfilled during this reign. At the end of one thousand years, the kingdom will be transferred from the Son to the Father (1 Cor 15:24-25) and it will merge with the eternal kingdom (Rev 20-21).</p>

<!-- gold band -->
<svg class="abs" style="left:0;top:1965px" width="1200" height="225" viewBox="0 0 1200 225">
  <path d="M0 0 H1200 V195 C 900 190 720 185 600 222 C 480 185 300 190 0 195 Z" fill="#cfb53b"/>
</svg>
<div class="abs band-text">If You Cannot Join Us In Person Click Here<br>For This Week,s Sermon</div>
<div class="btn btn-white" style="left:902px;top:2053px;width:158px;height:47px;box-shadow:none">Join Group</div>

<!-- visit -->
<div class="abs sec-title" style="top:2232px">Visit Us This Sunday</div>
<div class="abs sec-title" style="top:2272px;font-size:13px;font-weight:400">Flip The Boxes For More Information</div>
<div class="card" style="left:138px;top:2300px;width:277px;height:315px">
  <div class="card-img" role="img" aria-label="Candlelit sanctuary during morning worship" style="background:linear-gradient(#c9822c,#5a2f12 60%,#1e1009)"></div>
  <h3 style="top:218px">Morning Worship Service</h3>
  <div class="meta" style="top:242px">11:00 AM</div>
  <div class="small" style="top:268px">Sunday morning worship and service takes place in the main sanctuary.</div>
</div>
<div class="card card-gold" style="left:453px;top:2335px;width:290px;height:315px">
  <div class="card-img" role="img" aria-label="Church members sharing lunch together" style="background:linear-gradient(135deg,#9a6a3e,#3c2a20 55%,#6a4a30)"></div>
  <h3 style="top:218px">All Church Lunch</h3>
  <div class="meta" style="top:242px">12:15 PM</div>
  <div class="small" style="top:268px">Please join us for lunch after the service. Everyone is welcome!</div>
</div>
<div class="card" style="left:768px;top:2300px;width:290px;height:315px">
  <div class="card-img" role="img" aria-label="Adults gathered for Bible study beside stained glass" style="background:linear-gradient(135deg,#3e6a8a,#a07a3a 45%,#3a2a1c)"></div>
  <h3 style="top:218px">Afternoon Adult Bible Study</h3>
  <div class="meta" style="top:242px">12:45 PM</div>
  <div class="small" style="top:263px">TBA</div>
</div>

<!-- events -->
<div class="abs events"></div>
<div class="abs sec-title" style="top:2740px">Upcoming MFC Events</div>
<div class="ev-img" style="top:2825px;background:linear-gradient(135deg,#6a5a4a,#c8c0b0 50%,#5a4636)" role="img" aria-label="Study room with map on the wall"></div>
<div class="ev-date" style="top:2847px">January 21, 2026 @ 7:30 pm – 8:30 pm</div>
<div class="ev-title" style="top:2845px">7:30PM Wednesday Night Bible Study</div>
<div class="ev-line" style="top:2998px"></div>
<div class="ev-img" style="top:3046px;background:linear-gradient(135deg,#2c2620,#6a5648 50%,#8a6a4a)" role="img" aria-label="Fellowship hall with tables and chairs"></div>
<div class="ev-date" style="top:3068px">Febuary 1, 2026 @ 7:30 pm – 8:30 pm</div>
<div class="ev-title" style="top:3066px">11:00 AM Sunday Services</div>
<div class="ev-line" style="top:3219px"></div>
<div class="ev-img" style="top:3267px;background:linear-gradient(135deg,#4a4a3a,#dcdcd8 50%,#6a7a5a)" role="img" aria-label="White church entrance with arched door"></div>
<div class="ev-date" style="top:3289px">March 8, 2026 @ 11:00 pm – 12:30 pm</div>
<div class="ev-title" style="top:3287px">7:30PM Wednesday Night Bible Study</div>
<div class="ev-line" style="top:3440px"></div>

<!-- quote -->
<div class="abs quote">
  <p>We must meet the present situation, and we must speak a word to the world that no one else can speak. There are many reasons why we should do so. The need of the world, it's agony, it's pain, it's disease, call upon us to do so. But apart from that, it is our duty to do so.</p>
  <div class="who"><b>Elias Whitmore</b>, Your Content Goes Here</div>
</div>
<div class="abs avatar" role="img" aria-label="Portrait of the quoted preacher"></div>

<!-- sermons -->
<div class="abs sec-title" style="top:3823px">MFC Sermons</div>
<div class="card s-card" style="left:140px;top:3895px;width:290px;height:350px">
  <div class="s-img" role="img" aria-label="Glowing lantern in an old stone archway" style="background:radial-gradient(circle at 50% 35%,#e7a14a,#6a3a16 45%,#1a0e06)"></div>
  <h3>Jesus Saves us from the Wrath to Come</h3>
  <div class="meta">January 18, 2026</div>
  <div class="org">Meadowlark Fellowship Church</div>
</div>
<div class="card s-card" style="left:457px;top:3895px;width:290px;height:350px">
  <div class="s-img" role="img" aria-label="Vintage pocket watch above an open book" style="background:radial-gradient(circle at 50% 40%,#c8c8c4,#5a5a56 50%,#1e1e1c)"></div>
  <h3>Jesus Saves us from the Wrath to Come</h3>
  <div class="meta">January 18, 2026</div>
  <div class="org">Meadowlark Fellowship Church</div>
</div>
<div class="card s-card" style="left:772px;top:3895px;width:290px;height:350px">
  <div class="s-img" role="img" aria-label="Lantern and candles beside an open book" style="background:radial-gradient(circle at 35% 60%,#d88a2a,#4a2610 45%,#0e0804)"></div>
  <h3>A New Song for a Renewed World</h3>
  <div class="meta">January 11 2026</div>
  <div class="org">Meadowlark Fellowship Church</div>
</div>

<!-- footer -->
<svg class="abs" style="left:0;top:4295px" width="1200" height="448" viewBox="0 0 1200 448">
  <path d="M0 82 C 300 40 450 10 600 2 C 750 10 900 40 1200 82 V448 H0 Z" fill="#0a0a0a"/>
  <line x1="125" y1="388" x2="1071" y2="388" stroke="#888" stroke-width="1"/>
</svg>
<div class="abs foot-brand"><span class="brand-dot"></span><span>MEADOWLARK<br>FELLOWSHIP</span></div>
<div class="foot-col" style="left:508px"><h4>Ministries</h4><ul><li>Kids</li><li>Students</li><li>Worship</li><li>Women</li><li>Missions</li><li>Lifegroups</li></ul></div>
<div class="foot-col" style="left:702px"><h4>Ministries</h4><ul><li>Location &amp; Service Times</li><li>Next Steps</li><li>Vision &amp; Beliefs</li><li>Leadership</li><li>First Time Guest Survey</li><li>FAQ</li></ul></div>
<div class="foot-col" style="left:950px"><h4>Usefull Links</h4><ul><li>Photo Stream</li><li>Community Page</li><li>Quick Updates</li><li>Video Channel</li></ul></div>
<div class="abs copy">© Copy Right 2026 | All Right Reserved</div>

</body>
</html>
```